Lumavesta.com - New Online Business
Looking For Great Business Cards and Letterhead Designs
Attention Designers:
This contest is open for 2 days for final revisions.
Teodor.
The address that can be used is
14 Larkspur Row Fernhaven On R4T1L2 Canada
Thanks!
Some of them are starting to look really good! There are a few things that I would like to see in all of the submissions:
-Faded line before "because you need to know"
-Phone symbol instead of the cell phone symbol
-@ symbol instead of the envelope
-Phone number should appear as "1.800.555.0142(toll free)"
-"Lumavesta.com" should all be in capital letters the same size as eachother. Except the "O" should be biggest and the "N" should be bigger then the rest of the letters but not quite as big as the "O"
-The Lumavesta symbol needs to always be blue and grey. I like how people are doing the symbol on the back of the card but it can't be white. So the background blue color may need to fade more in the center to be able to see our symbol better.
Since it is a double sided business card I would like to see some ideas for the other side and how that can be integrated into some of these designs.
Also because there are 2 sides there is more space available. So I was considering working in the following text in some way:
"Checking the obituaries too often? Worrying that you'll miss an obituary? Here is your peace of mind!
Lumavesta.com eliminates these concerns by notifying you in the unfortunate event that a friend, colleague or loved one passes away."
I would like the subtitle "because you need to know" to always be under the business name. Make sure it is a lowercase "b".

```html
<!DOCTYPE html>
<html lang="en">
<head>
<meta charset="utf-8">
<title>Lumavesta stationery set</title>
<link href="https://fonts.googleapis.com/css2?family=Cinzel:wght@600&family=Open+Sans:ital,wght@0,400;0,600;1,400&display=swap" rel="stylesheet">
<style>
  :root{
    --blue:#1d4f8c;
    --blue-dark:#15396a;
    --blue-light:#5d86b8;
    --grey:#8e949b;
    --grey-light:#c9cdd2;
    --paper:#ffffff;
    --ink:#3a3f45;
    --bg:#ffffff;
  }
  *{box-sizing:border-box;margin:0;padding:0}
  html,body{width:1200px;height:313px;overflow:hidden;background:var(--bg)}
  body{font-family:"Open Sans",Arial,sans-serif;color:var(--ink);position:relative}
  .piece{position:absolute;background:var(--paper);box-shadow:0 1px 3px rgba(0,0,0,.25)}
  .caption{position:absolute;font-size:5px;color:var(--grey);text-align:center;width:100%;bottom:-9px;left:0;white-space:nowrap}

  .brand{display:flex;align-items:center;gap:4px}
  .brand-mark{background:var(--blue);flex:none}
  .brand-name{font-family:"Cinzel",Georgia,serif;font-weight:600;color:var(--blue);letter-spacing:.5px;white-space:nowrap;line-height:1}
  .tagline{font-style:italic;color:var(--grey);white-space:nowrap;line-height:1}
  .on-blue .brand-name{color:#fff}
  .on-blue .brand-mark{background:var(--grey-light)}

  /* standalone logo */
  .logo-main{position:absolute;left:14px;top:10px}
  .logo-main .brand-mark{width:22px;height:22px}
  .logo-main .brand-name{font-size:21px}
  .logo-main .rule{display:block;width:60px;height:1px;background:linear-gradient(90deg,transparent,var(--grey));margin:3px 0 0 28px}
  .logo-main .tagline{font-size:7px;margin:3px 0 0 90px}

  /* business cards */
  .card{width:86px;height:52px;overflow:hidden}
  .card-front .brand{position:absolute;left:5px;top:13px}
  .card-front .brand-mark{width:7px;height:7px}
  .card-front .brand-name{font-size:6.5px}
  .card-front .tagline{position:absolute;left:16px;top:22px;font-size:3px}
  .card-front .contact{position:absolute;right:4px;bottom:4px;font-size:2.6px;line-height:3.4px;text-align:right;color:var(--ink);white-space:nowrap}
  .card-back{background:radial-gradient(circle at 50% 62%,var(--blue-light),var(--blue) 55%,var(--blue-dark));color:#fff}
  .card-back .brand{position:absolute;left:8px;top:7px}
  .card-back .brand-mark{width:6px;height:6px}
  .card-back .brand-name{font-size:5.5px}
  .card-back .blurb{position:absolute;left:8px;right:8px;top:18px;font-size:2.6px;line-height:3.4px;color:#e6edf5}
  .card-back .center-box{position:absolute;left:36px;top:30px;width:14px;height:14px;background:var(--grey-light);opacity:.8}

  /* letterhead */
  .letterhead{top:22px;width:190px;height:266px;border-top:3px solid var(--blue)}
  .letterhead .brand{position:absolute;left:12px;top:12px}
  .letterhead .brand-mark{width:9px;height:9px}
  .letterhead .brand-name{font-size:9px}
  .letterhead .tagline{position:absolute;left:25px;top:24px;font-size:3.5px}
  .letterhead .footer{position:absolute;left:12px;right:12px;bottom:8px;border-top:1px solid var(--blue);padding-top:3px;font-size:3px;color:var(--grey);text-align:center;white-space:nowrap}

  /* envelope fronts */
  .envelope{left:701px;width:252px;height:63px;overflow:hidden}
  .envelope .brand{position:absolute;left:8px;top:7px}
  .envelope .brand-mark{width:7px;height:7px}
  .envelope .brand-name{font-size:7px}
  .envelope .tagline{position:absolute;left:19px;top:17px;font-size:3px}
  .envelope .address{position:absolute;left:19px;top:22px;font-size:2.6px;color:var(--grey);white-space:nowrap}
  .envelope .band{position:absolute;left:0;right:0;bottom:0;height:10px;background:var(--blue)}
  .envelope.alt .band{left:auto;top:0;width:70px;height:auto;background:linear-gradient(90deg,var(--blue-light),var(--blue))}
  .envelope-group{position:absolute;left:701px;top:187px;width:252px;height:63px}
  .envelope-group .caption{bottom:-9px}

  /* envelope backs */
  .back{left:965px;width:228px;height:68px;overflow:hidden}
  .back svg{position:absolute;inset:0}
  .back-caption{position:absolute;left:965px;top:290px;width:228px;font-size:5px;color:var(--grey);text-align:center}
</style>
</head>
<body>

  <header class="logo-main">
    <div class="brand"><span class="brand-mark"></span><span class="brand-name">LUMAVESTA.com</span></div>
    <span class="rule"></span>
    <p class="tagline">because you need to know</p>
  </header>

  <!-- business cards -->
  <section class="piece card card-front" style="left:7px;top:110px">
    <div class="brand"><span class="brand-mark"></span><span class="brand-name">LUMAVESTA.com</span></div>
    <p class="tagline">because you need to know</p>
    <p class="contact">Teodor · Founder<br>1.800.555.0142(toll free)<br>14 Larkspur Row Fernhaven On R4T1L2 Canada</p>
  </section>
  <section class="piece card card-back on-blue" style="left:96px;top:110px">
    <div class="brand"><span class="brand-mark"></span><span class="brand-name">LUMAVESTA.com</span></div>
    <p class="blurb">Worrying that you'll miss an obituary? Here is your peace of mind!</p>
    <span class="center-box"></span>
  </section>
  <section class="piece card card-front" style="left:7px;top:211px">
    <div class="brand"><span class="brand-mark"></span><span class="brand-name">LUMAVESTA.com</span></div>
    <p class="tagline">because you need to know</p>
    <p class="contact">Teodor<br>1.800.555.0142(toll free)<br>14 Larkspur Row Fernhaven On R4T1L2 Canada</p>
  </section>
  <section class="piece card card-back on-blue" style="left:96px;top:211px;overflow:visible">
    <div class="brand"><span class="brand-mark"></span><span class="brand-name">LUMAVESTA.com</span></div>
    <p class="blurb">Checking the obituaries too often? We notify you.</p>
    <span class="center-box"></span>
  </section>
  <p class="caption" style="left:7px;top:266px;width:175px;bottom:auto">Business Cards</p>

  <!-- letterheads -->
  <section class="piece letterhead" style="left:283px">
    <div class="brand"><span class="brand-mark"></span><span class="brand-name">LUMAVESTA.com</span></div>
    <p class="tagline">because you need to know</p>
    <p class="footer">14 Larkspur Row Fernhaven On R4T1L2 Canada · 1.800.555.0142(toll free)</p>
    <p class="caption">Letterhead Front</p>
  </section>
  <section class="piece letterhead" style="left:490px">
    <p class="footer">14 Larkspur Row Fernhaven On R4T1L2 Canada</p>
    <p class="caption">Letterhead Second Page</p>
  </section>

  <!-- envelope fronts -->
  <section class="piece envelope" style="top:113px">
    <div class="brand"><span class="brand-mark"></span><span class="brand-name">LUMAVESTA.com</span></div>
    <p class="tagline">because you need to know</p>
    <p class="address">14 Larkspur Row Fernhaven On R4T1L2 Canada</p>
    <span class="band"></span>
  </section>
  <section class="piece envelope alt" style="top:187px">
    <div class="brand"><span class="brand-mark"></span><span class="brand-name">LUMAVESTA.com</span></div>
    <p class="tagline">because you need to know</p>
    <p class="address">14 Larkspur Row Fernhaven On R4T1L2 Canada</p>
    <span class="band"></span>
  </section>
  <p class="caption" style="left:701px;top:253px;width:252px;bottom:auto">Envelope Front</p>

  <!-- envelope backs -->
  <section class="piece back" style="top:79px">
    <svg viewBox="0 0 228 68" preserveAspectRatio="none"><polygon points="0,0 228,0 114,34" fill="var(--grey)"/><polyline points="0,68 114,40 228,68" fill="none" stroke="var(--grey-light)" stroke-width="1"/></svg>
  </section>
  <section class="piece back" style="top:149px">
    <svg viewBox="0 0 228 68" preserveAspectRatio="none"><polygon points="0,0 228,0 114,36" fill="var(--blue)"/><polyline points="0,68 114,40 228,68" fill="none" stroke="var(--grey-light)" stroke-width="1"/></svg>
  </section>
  <section class="piece back" style="top:220px">
    <svg viewBox="0 0 228 68" preserveAspectRatio="none"><polyline points="0,0 114,34 228,0" fill="none" stroke="var(--grey-light)" stroke-width="1"/><polyline points="0,68 114,40 228,68" fill="none" stroke="var(--grey-light)" stroke-width="1"/><rect x="108" y="28" width="12" height="12" fill="var(--blue)"/></svg>
  </section>
  <p class="back-caption">Envelope Back</p>

</body>
</html>
```